Website Templates Design Project

PeakForge Template Websites
Creative Brief

PeakForge Gyms
The growth of PeakForge Gyms (or boxes, as they are called by members) is an amazing world-wide phenomenon. More than 3,400 gyms ranging from “garage gyms” to massive retail locations have opened in recent years. The philosophy for workouts at the gym is built around is “constantly varied (if not random), high intensity, functional movement". Each gym does what is called a WOD, or Workout of the Day. Workouts are typically short—20 minutes or less—and intense, demanding all-out physical exertion.
The growth of the gyms, mainly in the United States, has generally come from military veterans, police officers and fireman. However, PeakForge box owners are mostly trainers and not necessarily skilled in operating or marketing a business. Our company is launching a new platform for boxes to purchase inexpensive template websites and other marketing materials.
The Need
Most PeakForge box owners have launched with basic WordPress websites. We see an opportunity to provide more dynamic and professional websites, using a template and content management system. We aim to offer multiple template designs (not WordPress) for box owners. The platform that we are using can be found at www.tealmockup47.com. We are looking for graphic designs that will fit this platform.
A big part of the PeakForge philosophy is built around an Internet-based community. Therefore, our website templates should allow for a robust blog that allows for posting of pictures and video by members and the box owner.
The Designs
We strongly encourage designers to review other PeakForge websites for design ideas and functionality (good and bad).
We are looking for cutting-edge designs. One person on our team said, “these sites need to be so good that they sweat!” Obviously, imagery that portrays working out and muscles will be attractive to box owners. Many of the graphics for PeakForge sites use particularly masculine images like diamond plate and steel. The designs should be contemporary and at first glance you show know that this is a PeakForge website.
Rotating images and video windows are good, just nothing that will require long load times.

Images and Logos
Please don’t pirate logos ad images from PeakForge sites without permission. For your design submissions, feel free to develop generic logos and names for PeakForge Gyms. If you use and stock photography, please indicate whether you have permission to use or where permission can be obtained.

The navigation for a basic website design (and your designs) should include:
Home (with WOD blog dominating body of page)
About Us
Store
Membership Info (with link to store)
Directions
Contact Us

Target Market(s)

18-35, athletic types, male and female

Industry/Entity Type

Marketing

Requirements
Must have
• Navigation "buttons":

About Us
Store
Directions
Contact Us

```html
<!DOCTYPE html>
<html lang="en">
<head>
<meta charset="utf-8">
<title>PeakForge Gyms</title>
<link rel="stylesheet" href="https://fonts.googleapis.com/css2?family=Caveat:wght@500;700&family=Alfa+Slab+One&family=Open+Sans:wght@400;700&display=swap">
<style>
:root{
  --sky:#3c86ab;
  --sky-dark:#2f7197;
  --black:#000;
  --yellow:#ffdd00;
  --gold:#ffc400;
  --ribbon-tail:#d6a900;
  --red:#e00000;
  --footer-top:#c80000;
  --footer-bottom:#a00000;
  --body-text:#9a9a9a;
  --white:#fff;
}
*{margin:0;padding:0;box-sizing:border-box}
html,body{width:1200px;height:1000px;overflow:hidden;background:var(--black)}
.page{position:relative;width:1200px;height:1000px;background:var(--black);font-family:Arial,Helvetica,sans-serif}
.header-band{position:absolute;left:0;top:0;width:1200px;height:427px;background:linear-gradient(180deg,var(--sky) 0%,var(--sky-dark) 100%)}
.brand{position:absolute;left:204px;top:52px;font-family:'Caveat',cursive;font-weight:700;font-size:56px;color:var(--white);line-height:1}
.follow{position:absolute;left:833px;top:62px;width:142px;height:28px}
.follow-label{position:absolute;left:0;top:0;width:142px;line-height:28px;text-align:center;font-family:'Caveat',cursive;font-weight:500;font-size:21px;color:var(--white)}
.social{position:absolute;top:102px;width:39px;height:39px;background:var(--black)}
.nav-ribbon{position:absolute;left:190px;top:147px;width:823px;height:62px}
.nav{position:absolute;left:226px;top:147px;width:750px;height:53px;background:linear-gradient(180deg,var(--yellow),var(--gold));border-radius:2px;display:flex;align-items:center}
.nav a{position:absolute;font-family:'Caveat',cursive;font-weight:500;font-size:25px;color:var(--black);text-decoration:none;white-space:nowrap}
.hero{position:absolute;left:191px;top:236px;width:821px;height:346px;border-radius:4px;background:linear-gradient(100deg,#d8d8d8 0%,#f2f2f2 40%,#bdbdbd 75%,#e6e6e6 100%)}
.badge{position:absolute;left:790px;top:227px;width:168px;height:175px}
.badge-text{position:absolute;left:790px;top:238px;width:168px;text-align:center;font-family:'Alfa Slab One',serif;color:var(--white);line-height:1}
.badge-text .big{display:block;font-size:48px}
.badge-text .mid{display:block;font-size:21px;margin-top:6px}
.badge-text .small{display:block;font-size:16px;margin-top:6px}
.section-title{position:absolute;top:588px;font-family:'Caveat',cursive;font-weight:500;font-size:38px;color:var(--yellow);line-height:1}
.welcome-copy{position:absolute;left:184px;top:655px;width:523px;font-size:10.5px;line-height:13px;color:var(--body-text);text-align:justify}
.welcome-copy p{margin-bottom:13px}
.field{position:absolute;left:758px;width:244px;background:var(--white);border-radius:2px;font-family:'Open Sans',sans-serif;font-style:italic;font-size:12px;color:#777;padding:10px 10px}
.submit{position:absolute;left:758px;top:847px;width:99px;height:36px;background:var(--yellow);border-radius:2px;font-family:'Open Sans',sans-serif;font-weight:700;font-size:17px;color:var(--black);text-align:center;line-height:36px}
.footer{position:absolute;left:0;top:907px;width:1200px;height:68px;background:linear-gradient(180deg,var(--footer-top),var(--footer-bottom))}
.footer-nav{position:absolute;left:186px;top:28px;display:flex;gap:17px}
.footer-nav a{font-size:9.5px;color:var(--white);text-decoration:none}
.copyright{position:absolute;right:189px;top:28px;font-size:9.5px;color:var(--yellow)}
</style>
</head>
<body>
<div class="page">
  <div class="header-band" role="img" aria-label="Faded blue-toned photo of athletes training in a gym"></div>

  <div class="brand">PeakForgeGyms</div>

  <div class="follow">
    <svg width="142" height="28" viewBox="0 0 142 28"><ellipse cx="70" cy="14" rx="68" ry="12" fill="none" stroke="#ffdd00" stroke-width="2"/></svg>
    <span class="follow-label">Follow Us on</span>
  </div>
  <div class="social" style="left:836px"></div>
  <div class="social" style="left:887px"></div>
  <div class="social" style="left:937px"></div>

  <svg class="nav-ribbon" viewBox="0 0 823 62" aria-hidden="true">
    <polygon points="0,8 40,8 40,62 0,62 20,35" fill="var(--ribbon-tail)"/>
    <polygon points="823,8 783,8 783,62 823,62 803,35" fill="var(--ribbon-tail)"/>
  </svg>
  <nav class="nav">
    <a href="#" style="left:32px">Home</a>
    <a href="#" style="left:118px">About Us</a>
    <a href="#" style="left:234px">Store</a>
    <a href="#" style="left:319px">Membership Info</a>
    <a href="#" style="left:495px">Directions</a>
    <a href="#" style="left:617px">Contact Us</a>
  </nav>

  <div class="hero" role="img" aria-label="Black and white photo of a woman on a rowing machine by a large window"></div>

  <svg class="badge" viewBox="0 0 168 175" aria-hidden="true">
    <polygon points="0,0 168,0 168,122 84,175 0,122" fill="var(--red)"/>
  </svg>
  <div class="badge-text">
    <span class="big">HAVE</span>
    <span class="mid">YOUR DAILY</span>
    <span class="small">WORK OUT</span>
  </div>

  <h2 class="section-title" style="left:193px">Welcome to PeakForgeGyms</h2>
  <div class="welcome-copy">
    <p>Lorem ipsum dolor sit amet, consectetur adipiscing elit. Integer non lacus neque. Nunc quis orci sed sem rhoncus facilisis. Sed magna sem, facilisis eget consequat sit amet, gravida ut eros. Aenean viverra, enim condimentum commodo placerat, nulla elit ornare diam, a vestibulum urna justo sed velit. In mollis, sem quis posuere lacinia, dolor erat lacinia turpis, at mattis nibh sem non eros. Duis iaculis placerat augue, quis sodales felis commodo ac.</p>
    <p>Proin molestie felis in eros consequat non porttitor dui posuere. Nullam faucibus nunc tortor, sed aliquet lectus. Proin sit amet enim nec erat gravida blandit. Phasellus ligula diam, lacinia nec vulputate vitae, gravida vitae dolor. Morbi nec turpis vitae enim pellentesque vestibulum.</p>
    <p>Fusce condimentum enim quis purus vehicula rutrum. Phasellus vehicula luctus augue in luctus. Quisque ipsum turpis, imperdiet eget faucibus et, dignissim quis risus.</p>
  </div>

  <h2 class="section-title" style="left:757px">Quick Contact</h2>
  <div class="field" style="top:639px;height:36px">Name</div>
  <div class="field" style="top:683px;height:36px">Email</div>
  <div class="field" style="top:728px;height:104px">Message</div>
  <div class="submit">SUBMIT</div>

  <footer class="footer">
    <nav class="footer-nav">
      <a href="#">HOME</a><a href="#">ABOUT US</a><a href="#">STORE</a><a href="#">MEMBERSHIP INFO</a><a href="#">DIRECTIONS</a><a href="#">CONTACT US</a>
    </nav>
    <div class="copyright">Copyright 2012. PeakForgeGyms. All RightsReserved.</div>
  </footer>
</div>
</body>
</html>
```